complete redesign of brimlearn.com , responsive design

Present website should be used for ideation purpose, designer should submit best design which can explain visitor and excite them to download the app.
. By looking at default view of website, students should get the idea about product.

This website to explain about tablet app and it's features, benefits for students, parents and institutes.

This is tablet/Nuvo based product to prepare National ( KVL, ORBLX, DUN, Veltorian etc) and International competitive exams (PYX, HUM, WOB, FLUD etc) and visitor should get ideas by just looking at the home page.

Institutes can publish their content on eQuorra.

Student can optimize time and performance on eQuorra.

Content is same as present website and please use app screenshot to explain the product. screens should be used wherever relevant, refer attached screens. Website must be responsive and easy in navigation.
This is cloud based system and offering prep test , analysis and dynamic testing as per their study plan.

Target Market(s)

Education

Industry/Entity Type

Education

Coding

Coded - Design and coding required

Number of Pages Required

5+ page

Colors
6b449b
886aae
b7a5cd
e4daeb
f3f1f8
ffffff

Requirements
Must have
• Great design , responsive, easy to grasp the idea. Allow option to register for free app download.
• Project must have all pages as it is in present website.
Nice to have
• I will leave designer to come up with presentation.
Should not have
• It should not be layout as it is today. Lot of design being submitted by changing just color and icons. I request to come up with your style and you can use contents from present website.

```html
<!DOCTYPE html>
<html lang="en">
<head>
<meta charset="utf-8">
<title>eQuorra – Home</title>
<link rel="stylesheet" href="https://fonts.googleapis.com/css2?family=Open+Sans:wght@400;600;700&display=swap">
<style>
:root{
  --purple:#6b449b;
  --purple-mid:#886aae;
  --purple-soft:#b7a5cd;
  --lilac:#e4daeb;
  --mist:#f3f1f8;
  --white:#ffffff;
  --ink:#3b3b3b;
  --grey:#8a8a8a;
  --sky:#7fd3f0;
  --line:#e6e3ec;
}
*{box-sizing:border-box;margin:0;padding:0}
html,body{width:811px;height:1200px;overflow:hidden}
body{background:var(--mist);font-family:"Open Sans",Arial,sans-serif;color:var(--ink);position:relative}
.site-header{position:absolute;left:0;top:0;width:811px;height:70px}
.brand{position:absolute;left:100px;top:14px}
.brand-name{font-size:24px;font-weight:700;color:var(--purple);line-height:1}
.brand-tagline{font-size:7px;color:var(--purple-mid);letter-spacing:1px;margin-top:3px}
.main-nav{position:absolute;left:228px;top:0;width:488px;height:36px;background:var(--white);display:flex;align-items:center;box-shadow:0 1px 3px rgba(0,0,0,.08)}
.main-nav a{flex:1;text-align:center;font-size:8px;color:var(--grey);text-decoration:none;height:36px;line-height:36px;white-space:nowrap}
.main-nav a.is-active{background:var(--sky);color:var(--white)}
.main-nav .nav-search{flex:0 0 26px;display:flex;align-items:center;justify-content:center}
.card{position:absolute;width:115px;background:var(--white);box-shadow:0 1px 3px rgba(60,40,90,.12);overflow:hidden}
.card-media{width:100%;display:block}
.card-body{padding:6px 7px}
.card-title{font-size:7.5px;font-weight:600;color:var(--ink);line-height:1.35}
.card-meta{display:flex;gap:8px;margin-top:5px;font-size:6px;color:var(--grey);align-items:center}
.card-meta span{display:flex;align-items:center;gap:2px}
.card-meta i{display:inline-block;width:6px;height:5px;background:var(--purple-mid);border-radius:1px}
.card-text{font-size:6px;color:var(--grey);line-height:1.5;margin-top:5px}
.card-link{font-size:6px;color:var(--purple);font-weight:600;margin-top:4px;display:block}
.g-sky{background:linear-gradient(135deg,#dfeaf6,#9fc3e6)}
.g-warm{background:linear-gradient(135deg,#e9c9a6,#b07a55)}
.g-color{background:linear-gradient(135deg,#e85aa0,#4a8fe0 55%,#f3c84a)}
.g-books{background:linear-gradient(160deg,#c98d52,#7a4b2a)}
.g-room{background:linear-gradient(135deg,#cfe0c8,#8bb0a0)}
.g-board{background:linear-gradient(135deg,#4c5a54,#9aa89e)}
.g-glow{background:linear-gradient(135deg,#2a2350,#e07a2e 60%,#f6d24a)}
.app-banner{position:absolute;left:100px;top:567px;width:355px;height:157px;background:var(--white);box-shadow:0 1px 3px rgba(60,40,90,.12);display:flex}
.app-screen{flex:1;padding:10px;background:var(--mist)}
.app-screen .bar{height:6px;background:var(--purple);margin-bottom:6px}
.app-screen .row{height:4px;background:var(--purple-soft);margin:5px 0;border-radius:2px}
.app-screen .row.red{background:#e06a6a;width:70%}
.app-panel{width:130px;background:var(--purple);color:var(--white);padding:14px 12px}
.app-panel h3{font-size:10px;font-weight:700;margin-bottom:6px}
.app-panel p{font-size:6.5px;line-height:1.5;color:var(--lilac)}
.register-box{position:absolute;left:608px;top:430px;width:115px;height:150px;background:var(--purple);color:var(--white);padding:10px 9px}
.register-box h3{font-size:9px;font-weight:700;line-height:1.3}
.register-box p{font-size:6px;color:var(--lilac);line-height:1.5;margin-top:6px}
.register-box .field{height:12px;background:var(--white);margin-top:8px;border-radius:2px}
.register-box .btn{display:inline-block;margin-top:6px;background:var(--purple-mid);font-size:6.5px;padding:3px 8px;border-radius:2px}
.loader{position:absolute;left:395px;top:1090px}
.site-footer{position:absolute;left:0;top:1140px;width:811px;height:60px;background:var(--purple);display:flex;align-items:center;padding:0 100px}
.footer-brand{font-size:16px;font-weight:700;color:var(--white)}
.footer-links{flex:1;text-align:center}
.footer-links nav{display:flex;justify-content:center;gap:10px;font-size:6.5px;color:var(--white)}
.footer-links small{display:block;font-size:5.5px;color:var(--lilac);margin-top:4px}
.footer-social{display:flex;gap:6px}
.footer-social span{width:14px;height:14px;border-radius:50%;background:var(--purple-mid);display:block}
</style>
</head>
<body>
<header class="site-header">
  <div class="brand"><div class="brand-name">eQuorra</div><div class="brand-tagline">PREPARE TO WIN</div></div>
  <nav class="main-nav">
    <a class="is-active">Home</a><a>News</a><a>Notifications</a><a>Suggestions</a><a>Test</a><a>Results</a><a>Forum</a><a>Login</a>
    <span class="nav-search"><svg width="10" height="10" viewBox="0 0 10 10"><circle cx="4" cy="4" r="3" fill="none" stroke="#8a8a8a" stroke-width="1.2"/><line x1="6.2" y1="6.2" x2="9" y2="9" stroke="#8a8a8a" stroke-width="1.2"/></svg></span>
  </nav>
</header>

<main class="feed">
  <!-- column 1 -->
  <article class="card" style="left:100px;top:81px;height:203px">
    <div class="card-media g-sky" style="height:128px" role="img" aria-label="Study book package"></div>
    <div class="card-body"><div class="card-title">Mathematics<br>Algebra Practice</div>
    <div class="card-meta"><span><i></i>12 Comments</span><span><i></i>10 Ratings</span></div>
    <div class="card-text">Practice sets for every chapter.</div></div>
  </article>
  <article class="card" style="left:100px;top:289px;height:264px">
    <div class="card-media g-warm" style="height:95px" role="img" aria-label="Student reading at a desk"></div>
    <div class="card-body"><div class="card-title">Lorem Ipsum is simply dummy text of the printing and setting</div>
    <div class="card-meta"><span><i></i>12 Comments</span><span><i></i>10 Ratings</span></div>
    <div class="card-text">Lorem ipsum dolor sit amet, consectetur adipiscing elit sed do eiusmod tempor incididunt ut labore et dolore magna.</div>
    <span class="card-link">Know more</span></div>
  </article>
  <article class="card" style="left:100px;top:729px;height:203px">
    <div class="card-media g-room" style="height:88px" role="img" aria-label="Student with tablet"></div>
    <div class="card-body"><div class="card-title">Lorem Ipsum is simply dummy text of the printing and setting</div>
    <div class="card-meta"><span><i></i>12 Comments</span><span><i></i>10 Ratings</span></div>
    <div class="card-text">Sed ut perspiciatis unde omnis iste natus error sit voluptatem.</div></div>
  </article>
  <article class="card" style="left:100px;top:940px;height:140px">
    <div class="card-media g-sky" style="height:82px" role="img" aria-label="Study book package"></div>
    <div class="card-body"><div class="card-title">Lorem Ipsum is simply dummy text of the printing and setting</div>
    <div class="card-meta"><span><i></i>12 Comments</span><span><i></i>10 Ratings</span></div></div>
  </article>

  <!-- column 2 -->
  <article class="card" style="left:227px;top:81px;height:189px">
    <div class="card-media g-color" style="height:100px" role="img" aria-label="Colourful digital reading scene"></div>
    <div class="card-body"><div class="card-title">Digital Reading…<br>Digital Education</div>
    <div class="card-meta"><span><i></i>12 Comments</span><span><i></i>10 Ratings</span></div>
    <div class="card-text">Learn anywhere with interactive lessons on tablet.</div></div>
  </article>
  <article class="card" style="left:227px;top:275px;height:278px">
    <div class="card-media g-warm" style="height:110px" role="img" aria-label="Hands writing notes"></div>
    <div class="card-body"><div class="card-title">Lorem Ipsum is simply dummy text of the printing and setting</div>
    <div class="card-meta"><span><i></i>12 Comments</span><span><i></i>10 Ratings</span></div>
    <div class="card-text">Ut enim ad minim veniam, quis nostrud exercitation ullamco laboris nisi ut aliquip ex ea commodo.</div>
    <span class="card-link">Know more</span></div>
  </article>
  <article class="card" style="left:227px;top:729px;height:203px">
    <div class="card-media g-board" style="height:100px" role="img" aria-label="Student at a chalkboard"></div>
    <div class="card-body"><div class="card-title">Lorem Ipsum is simply dummy text of the printing and setting</div>
    <div class="card-meta"><span><i></i>12 Comments</span><span><i></i>10 Ratings</span></div>
    <div class="card-text">Nemo enim ipsam voluptatem quia voluptas sit.</div></div>
  </article>
  <article class="card" style="left:227px;top:940px;height:126px">
    <div class="card-media g-color" style="height:74px" role="img" aria-label="Colourful learning scene"></div>
    <div class="card-body"><div class="card-title">Lorem Ipsum is simply dummy text of the printing and setting</div>
    <div class="card-meta"><span><i></i>12 Comments</span><span><i></i>10 Ratings</span></div></div>
  </article>

  <!-- column 3 -->
  <article class="card" style="left:354px;top:81px;height:189px">
    <div class="card-media g-room" style="height:100px" role="img" aria-label="Student studying with books"></div>
    <div class="card-body"><div class="card-title">Lorem Ipsum is simply dummy text of the printing and setting</div>
    <div class="card-meta"><span><i></i>12 Comments</span><span><i></i>10 Ratings</span></div>
    <div class="card-text">Plan your study time and track progress.</div></div>
  </article>
  <article class="card" style="left:354px;top:275px;height:120px">
    <div class="card-media g-glow" style="height:70px" role="img" aria-label="Glowing digital book"></div>
    <div class="card-body"><div class="card-title">Lorem Ipsum is simply dummy text of the printing and setting</div>
    <div class="card-meta"><span><i></i>12 Comments</span><span><i></i>10 Ratings</span></div></div>
  </article>
  <article class="card" style="left:354px;top:400px;width:242px;height:155px">
    <div class="card-media" style="height:110px;background:var(--mist);padding:8px">
      <svg width="226" height="94" viewBox="0 0 226 94" role="img" aria-label="App results screen">
        <rect width="226" height="8" fill="#6b449b"/>
        <rect x="0" y="14" width="60" height="80" fill="#e4daeb"/>
        <rect x="70" y="16" width="150" height="5" fill="#b7a5cd"/>
        <rect x="70" y="28" width="120" height="5" fill="#b7a5cd"/>
        <rect x="70" y="44" width="14" height="40" fill="#886aae"/>
        <rect x="92" y="56" width="14" height="28" fill="#b7a5cd"/>
        <rect x="114" y="36" width="14" height="48" fill="#6b449b"/>
        <rect x="136" y="62" width="14" height="22" fill="#b7a5cd"/>
      </svg>
    </div>
    <div class="card-body"><div class="card-title">Lorem Ipsum is simply dummy text of the printing and setting</div></div>
  </article>
  <article class="card" style="left:354px;top:729px;height:203px">
    <div class="card-media g-warm" style="height:110px" role="img" aria-label="Student holding a tablet"></div>
    <div class="card-body"><div class="card-title">Lorem Ipsum is simply dummy text of the printing and setting</div>
    <div class="card-meta"><span><i></i>12 Comments</span><span><i></i>10 Ratings</span></div></div>
  </article>
  <article class="card" style="left:354px;top:940px;height:126px">
    <div class="card-media g-room" style="height:74px" role="img" aria-label="Student smiling with notes"></div>
    <div class="card-body"><div class="card-title">Lorem Ipsum is simply dummy text of the printing and setting</div></div>
  </article>

  <!-- column 4 -->
  <article class="card" style="left:481px;top:81px;height:189px">
    <div class="card-media g-room" style="height:100px" role="img" aria-label="Student portrait"></div>
    <div class="card-body"><div class="card-title">Lorem Ipsum is simply dummy text of the printing and setting</div>
    <div class="card-meta"><span><i></i>12 Comments</span><span><i></i>10 Ratings</span></div></div>
  </article>
  <article class="card" style="left:481px;top:275px;height:120px">
    <div class="card-media g-books" style="height:78px" role="img" aria-label="Stack of books"></div>
    <div class="card-body"><div class="card-title">Lorem Ipsum is simply dummy text of the printing and setting</div></div>
  </article>
  <article class="card" style="left:481px;top:567px;height:157px">
    <div class="card-media g-books" style="height:105px" role="img" aria-label="Books on a shelf"></div>
    <div class="card-body"><div class="card-title">Lorem Ipsum is simply dummy text of the printing and setting</div>
    <div class="card-meta"><span><i></i>12 Comments</span><span><i></i>10 Ratings</span></div></div>
  </article>
  <article class="card" style="left:481px;top:729px;height:203px">
    <div class="card-media g-sky" style="height:110px" role="img" aria-label="Student in a library"></div>
    <div class="card-body"><div class="card-title">Lorem Ipsum is simply dummy text of the printing and setting</div>
    <div class="card-meta"><span><i></i>12 Comments</span><span><i></i>10 Ratings</span></div></div>
  </article>
  <article class="card" style="left:481px;top:940px;height:140px">
    <div class="card-body"><div class="card-title">Score Analysis</div>
      <svg width="101" height="40" viewBox="0 0 101 40" style="margin-top:8px">
        <circle cx="16" cy="20" r="13" fill="none" stroke="#f0a23a" stroke-width="5"/>
        <circle cx="50" cy="20" r="13" fill="none" stroke="#5cbf6a" stroke-width="5"/>
        <circle cx="84" cy="20" r="13" fill="none" stroke="#886aae" stroke-width="5"/>
      </svg>
      <div class="card-text">Accuracy, speed and attempts per subject.</div>
      <div class="card-meta"><span><i></i>12 Comments</span><span><i></i>10 Ratings</span></div></div>
  </article>

  <!-- column 5 -->
  <article class="card" style="left:608px;top:81px;height:189px">
    <div class="card-media g-warm" style="height:100px" role="img" aria-label="Student smiling"></div>
    <div class="card-body"><div class="card-title">Lorem Ipsum is simply dummy text of the printing and setting</div>
    <div class="card-meta"><span><i></i>12 Comments</span><span><i></i>10 Ratings</span></div></div>
  </article>
  <article class="card" style="left:608px;top:275px;height:148px">
    <div class="card-body"><div class="card-title">Lorem Ipsum is simply dummy text of the printing and setting</div>
    <div class="card-meta"><span><i></i>12 Comments</span><span><i></i>10 Ratings</span></div>
    <div class="card-text">Duis aute irure dolor in reprehenderit in voluptate velit esse cillum dolore eu fugiat nulla pariatur.</div>
    <span class="card-link">Know more</span></div>
  </article>
  <aside class="register-box">
    <h3>Lorem Ipsum has been the industry standard text</h3>
    <p>Register free and get the app on your tablet.</p>
    <div class="field"></div>
    <span class="btn">Register</span>
  </aside>
  <article class="card" style="left:608px;top:590px;height:220px">
    <div class="card-media g-glow" style="height:150px" role="img" aria-label="Glowing digital book"></div>
    <div class="card-body"><div class="card-title">Lorem Ipsum is simply dummy text of the printing and setting</div>
    <div class="card-meta"><span><i></i>12 Comments</span><span><i></i>10 Ratings</span></div></div>
  </article>
  <article class="card" style="left:608px;top:815px;height:117px">
    <div class="card-body"><div class="card-title">Lorem Ipsum is simply dummy text of the printing and setting</div>
    <div class="card-meta"><span><i></i>12 Comments</span><span><i></i>10 Ratings</span></div>
    <div class="card-text">Excepteur sint occaecat cupidatat non proident sunt in culpa.</div></div>
  </article>
  <article class="card" style="left:608px;top:940px;height:126px">
    <div class="card-media g-color" style="height:74px" role="img" aria-label="Colourful learning scene"></div>
    <div class="card-body"><div class="card-title">Lorem Ipsum is simply dummy text of the printing and setting</div></div>
  </article>

  <!-- app feature banner -->
  <section class="app-banner">
    <div class="app-screen" role="img" aria-label="App test screen">
      <div class="bar"></div>
      <div class="row"></div><div class="row red"></div><div class="row" style="width:85%"></div>
      <div class="row" style="width:60%"></div><div class="row red" style="width:50%"></div>
      <div class="row"></div><div class="row" style="width:75%"></div>
    </div>
    <div class="app-panel">
      <h3>Test Instructions</h3>
      <p>Read each question carefully, manage your time and submit before the timer ends to see your instant analysis.</p>
    </div>
  </section>
</main>

<svg class="loader" width="20" height="20" viewBox="0 0 20 20" aria-hidden="true">
  <g fill="#8a8a8a"><circle cx="10" cy="2" r="1.5"/><circle cx="15.7" cy="4.3" r="1.4" opacity=".85"/><circle cx="18" cy="10" r="1.3" opacity=".7"/><circle cx="15.7" cy="15.7" r="1.2" opacity=".55"/><circle cx="10" cy="18" r="1.1" opacity=".45"/><circle cx="4.3" cy="15.7" r="1" opacity=".35"/><circle cx="2" cy="10" r="1" opacity=".25"/></g>
</svg>

<footer class="site-footer">
  <div class="footer-brand">eQuorra</div>
  <div class="footer-links">
    <nav><span>Home</span><span>Gallery</span><span>Achievements</span><span>Downloads</span><span>News</span><span>Terms</span><span>FAQ</span></nav>
    <small>© 2024 eQuorra. All rights reserved.</small>
  </div>
  <div class="footer-social"><span></span><span></span><span></span><span></span></div>
</footer>
</body>
</html>
```